Step and Repeat Backdrop for wedding reception photo booth

Would like to have a Step and Repeat Backdrop (8 foot high by 10 foot wide) that incorporates the wedding logo (attached) and the names Elena and Gavin. Background should be white, and wedding colors are burgundy and gold. Show me creativity :-) I have included some random samples.

```html
<!DOCTYPE html>
<html lang="en">
<head>
<meta charset="utf-8">
<title>Elena &amp; Gavin — Step and Repeat Backdrop</title>
<link rel="stylesheet" href="https://fonts.googleapis.com/css2?family=Playfair+Display:wght@400&display=swap">
<style>
  :root {
    --page: #ffffff;
    --burgundy: #8c0020;
    --gold: #c09a5e;
    --gold-light: #d6b981;
    --gold-deep: #a87f42;
    --flourish-tint: rgba(192, 154, 94, 0.28);
    --flourish-tint-soft: rgba(192, 154, 94, 0.16);
  }
  * { margin: 0; padding: 0; box-sizing: border-box; }
  html, body {
    width: 1200px;
    height: 1200px;
    overflow: hidden;
    background: var(--page);
  }
  .backdrop {
    position: absolute;
    left: 136px;
    top: 227px;
    width: 928px;
    height: 742px;
    background: var(--burgundy);
    overflow: hidden;
    font-family: "Playfair Display", "Times New Roman", serif;
  }
  .monogram {
    position: absolute;
    width: 50px;
    margin-left: -25px;
    margin-top: -11px;
    text-align: center;
    font-size: 16px;
    line-height: 22px;
    letter-spacing: -0.5px;
    color: var(--gold);
  }
  .flourish {
    position: absolute;
    left: 280px;
    width: 368px;
    height: 112px;
    border-radius: 56px;
    background: linear-gradient(90deg, var(--flourish-tint-soft), var(--flourish-tint) 50%, var(--flourish-tint-soft));
  }
  .flourish--top { top: 82px; }
  .flourish--bottom { top: 305px; }
  .couple-names {
    position: absolute;
    left: 0;
    width: 100%;
    top: 220px;
    text-align: center;
    font-size: 48px;
    line-height: 60px;
    font-weight: 400;
    letter-spacing: 1px;
    color: var(--gold);
    background: linear-gradient(90deg, var(--gold-deep), var(--gold-light) 50%, var(--gold-deep));
    -webkit-background-clip: text;
    background-clip: text;
    -webkit-text-fill-color: transparent;
  }
</style>
</head>
<body>
<main class="backdrop">
  <span class="monogram" style="left:30px;top:24px">E&amp;G</span>
  <span class="monogram" style="left:175px;top:24px">E&amp;G</span>
  <span class="monogram" style="left:319px;top:24px">E&amp;G</span>
  <span class="monogram" style="left:464px;top:24px">E&amp;G</span>
  <span class="monogram" style="left:608px;top:24px">E&amp;G</span>
  <span class="monogram" style="left:752px;top:24px">E&amp;G</span>
  <span class="monogram" style="left:897px;top:24px">E&amp;G</span>

  <span class="monogram" style="left:99px;top:106px">E&amp;G</span>
  <span class="monogram" style="left:243px;top:106px">E&amp;G</span>
  <span class="monogram" style="left:676px;top:106px">E&amp;G</span>
  <span class="monogram" style="left:820px;top:106px">E&amp;G</span>

  <span class="monogram" style="left:30px;top:197px">E&amp;G</span>
  <span class="monogram" style="left:175px;top:197px">E&amp;G</span>
  <span class="monogram" style="left:752px;top:197px">E&amp;G</span>
  <span class="monogram" style="left:897px;top:197px">E&amp;G</span>

  <span class="monogram" style="left:99px;top:278px">E&amp;G</span>
  <span class="monogram" style="left:820px;top:278px">E&amp;G</span>

  <span class="monogram" style="left:30px;top:369px">E&amp;G</span>
  <span class="monogram" style="left:175px;top:369px">E&amp;G</span>
  <span class="monogram" style="left:752px;top:369px">E&amp;G</span>
  <span class="monogram" style="left:897px;top:369px">E&amp;G</span>

  <span class="monogram" style="left:99px;top:451px">E&amp;G</span>
  <span class="monogram" style="left:243px;top:451px">E&amp;G</span>
  <span class="monogram" style="left:388px;top:451px">E&amp;G</span>
  <span class="monogram" style="left:532px;top:451px">E&amp;G</span>
  <span class="monogram" style="left:676px;top:451px">E&amp;G</span>
  <span class="monogram" style="left:820px;top:451px">E&amp;G</span>

  <span class="monogram" style="left:30px;top:542px">E&amp;G</span>
  <span class="monogram" style="left:175px;top:542px">E&amp;G</span>
  <span class="monogram" style="left:314px;top:542px">E&amp;G</span>
  <span class="monogram" style="left:460px;top:542px">E&amp;G</span>
  <span class="monogram" style="left:608px;top:542px">E&amp;G</span>
  <span class="monogram" style="left:752px;top:542px">E&amp;G</span>
  <span class="monogram" style="left:897px;top:542px">E&amp;G</span>

  <span class="monogram" style="left:99px;top:625px">E&amp;G</span>
  <span class="monogram" style="left:243px;top:625px">E&amp;G</span>
  <span class="monogram" style="left:388px;top:625px">E&amp;G</span>
  <span class="monogram" style="left:532px;top:625px">E&amp;G</span>
  <span class="monogram" style="left:676px;top:625px">E&amp;G</span>
  <span class="monogram" style="left:820px;top:625px">E&amp;G</span>

  <span class="monogram" style="left:30px;top:715px">E&amp;G</span>
  <span class="monogram" style="left:175px;top:715px">E&amp;G</span>
  <span class="monogram" style="left:319px;top:715px">E&amp;G</span>
  <span class="monogram" style="left:464px;top:715px">E&amp;G</span>
  <span class="monogram" style="left:608px;top:715px">E&amp;G</span>
  <span class="monogram" style="left:752px;top:715px">E&amp;G</span>
  <span class="monogram" style="left:897px;top:715px">E&amp;G</span>

  <div class="flourish flourish--top" role="img" aria-label="Gold scrollwork flourish with a fleur-de-lis at its centre, above the names"></div>
  <h1 class="couple-names">ELENA &amp; GAVIN</h1>
  <div class="flourish flourish--bottom" role="img" aria-label="Mirrored gold scrollwork flourish with a fleur-de-lis at its centre, below the names"></div>
</main>
</body>
</html>
```